New Property development signage

large poster for a new development.
3 metres x 2 metres. To include the following.

Varnock Meadows
TO LET
LUXURY FULLY FURNISHED LARGE
2 AND 3 BED APARTMENTS
Tilwick Estates
362 4159
www.tilwickestates-example.com

Need this to be large simple writing with Tilwick estates logo on the bottom

Target Market(s)

High end rental property market

Industry/Entity Type

Real Estate Development

Colors
000000
cbcbcb
0555a3

Requirements
Must have
• Name of the development must be in a different font, classic style
Nice to have
• Light Grey background, blues for colours
Should not have
• anymore than 3 /4 colours

```html
<!DOCTYPE html>
<html lang="en">
<head>
<meta charset="utf-8">
<title>Varnock Meadows – To Let Signage</title>
<link rel="stylesheet" href="https://fonts.googleapis.com/css2?family=Arimo:wght@400;700&family=Cinzel+Decorative:wght@700&family=Didact+Gothic&display=swap">
<style>
  :root {
    --brand-blue: #0555a3;
    --sign-grey: #cbcbcb;
    --ink: #000000;
    --backdrop: #eef1f4;
  }
  * { box-sizing: border-box; margin: 0; padding: 0; }
  html, body {
    width: 1200px;
    height: 1000px;
    overflow: hidden;
    background: var(--backdrop);
  }
  .sign {
    position: absolute;
    left: 75px;
    top: 150px;
    width: 1050px;
    height: 700px;
    display: flex;
    flex-direction: column;
  }
  .sign__header {
    height: 171px;
    background: var(--brand-blue);
    display: flex;
    align-items: center;
    justify-content: center;
  }
  .development-name {
    font-family: "Cinzel Decorative", "Times New Roman", serif;
    font-weight: 700;
    font-size: 74px;
    letter-spacing: 2px;
    color: var(--sign-grey);
  }
  .sign__headline {
    height: 248px;
    background: var(--sign-grey);
    display: flex;
    align-items: center;
    justify-content: center;
  }
  .to-let {
    font-family: "Didact Gothic", "Century Gothic", sans-serif;
    font-size: 232px;
    line-height: 1;
    color: var(--brand-blue);
    letter-spacing: 2px;
    transform: translateY(6px);
  }
  .sign__details {
    flex: 1;
    background: var(--brand-blue);
    display: flex;
    flex-direction: column;
    align-items: center;
    padding-top: 22px;
  }
  .offer {
    font-family: "Arimo", Arial, sans-serif;
    font-weight: 700;
    color: var(--sign-grey);
    font-size: 49px;
    line-height: 1.18;
    text-align: center;
    letter-spacing: 1px;
  }
  .offer__line--spaced { word-spacing: 14px; }
  .agent {
    margin-top: 40px;
    display: flex;
    align-items: center;
    gap: 22px;
  }
  .agent__mark {
    display: flex;
    align-items: center;
    gap: 10px;
    background: var(--brand-blue);
  }
  .agent__square {
    width: 30px;
    height: 30px;
    background: var(--sign-grey);
  }
  .agent__name-mark {
    font-family: "Arimo", Arial, sans-serif;
    font-weight: 700;
    font-size: 46px;
    color: var(--sign-grey);
  }
  .agent__contact {
    font-family: "Arimo", Arial, sans-serif;
    color: var(--ink);
    line-height: 1.25;
  }
  .agent__title { font-weight: 700; font-size: 22px; }
  .agent__line { font-size: 17px; letter-spacing: 1.5px; }
</style>
</head>
<body>
  <main class="sign">
    <header class="sign__header">
      <h1 class="development-name">VARNOCK MEADOWS</h1>
    </header>
    <section class="sign__headline">
      <p class="to-let">TO LET</p>
    </section>
    <section class="sign__details">
      <p class="offer">
        <span class="offer__line--spaced">LUXURY FULLY FURNISHED</span><br>
        LARGE 2 &amp; 3 BED APARTMENTS
      </p>
      <div class="agent">
        <div class="agent__mark">
          <span class="agent__square"></span>
          <span class="agent__name-mark">Tilwick</span>
        </div>
        <div class="agent__contact">
          <p class="agent__title">Tilwick Estates</p>
          <p class="agent__line">(01) 362 4159</p>
          <p class="agent__line">www.tilwickestates-example.com</p>
        </div>
      </div>
    </section>
  </main>
</body>
</html>
```